BLUE HAVEN (Business Card for Training Company)

Blue Haven is a training and consultancy company with a focus on executive protection and medical. I would like the card to be nice and sharp, not overdone and in black and red. I would also like it to highlight that it is "A Dravin Company"

I would like it to be simple and highlight a few things.

1. Name
2. Title
3. Phone Number
4. Email

I would also like www.dravinholdings.example/blue-haven to be on the card somewhere.

Target Market(s)

Security Companies

Industry/Entity Type

Security

Contact Information for Business Card

Blue Haven is a training and consultancy company with a focus on executive protection and medical. I would like the card to be nice and sharp, not overdone and in black and red. I would also like it to highlight that it is "A Dravin Company" I would like it to be simple and highlight a few things. 1. Name 2. Title 3. Phone Number 4. Email I would also like www.dravinholdings.example/blue-haven to be on the card somewhere.

Requirements
Must have
• A Dravin Company listed on the card and the website
Nice to have
• Highlight Medical Training, Consultancy & Executive Protection Courses

```html
<!DOCTYPE html>
<html lang="en">
<head>
<meta charset="utf-8">
<title>Blue Haven – Business Card</title>
<link rel="stylesheet" href="https://fonts.googleapis.com/css2?family=Roboto:wght@400;700;900&display=swap">
<style>
  :root {
    --maroon: #6b0f12;
    --maroon-dark: #4d0a0c;
    --maroon-line: #3c0708;
    --ink: #1a1a1a;
    --ink-soft: #555555;
    --paper: #ffffff;
    --backdrop: #e8e8ea;
  }
  * { box-sizing: border-box; margin: 0; padding: 0; }
  html, body {
    width: 1200px; height: 1200px; overflow: hidden;
    background: var(--backdrop);
    font-family: "Roboto", Arial, sans-serif;
  }
  .sheet {
    width: 1200px; height: 1200px;
    display: flex; flex-direction: column; align-items: center; justify-content: center;
    gap: 60px;
  }
  .card {
    position: relative; width: 900px; height: 514px; overflow: hidden;
    box-shadow: 0 6px 18px rgba(0,0,0,0.12);
  }

  /* Back */
  .card-back { background: var(--maroon); }
  .card-back .wordmark {
    position: absolute; left: 0; right: 0; top: 170px;
    display: flex; align-items: center; justify-content: center; gap: 12px;
  }
  .card-back .web-band {
    position: absolute; left: 0; right: 0; top: 340px; height: 70px;
    background: var(--maroon-dark);
    display: flex; align-items: center; padding-left: 90px; gap: 12px;
    color: var(--paper); font-size: 20px; letter-spacing: 0.3px;
  }

  .wordmark-square { width: 18px; height: 18px; background: currentColor; }
  .wordmark-name {
    font-weight: 900; font-size: 46px; line-height: 1; letter-spacing: 1px;
  }
  .card-back .wordmark { color: var(--paper); }

  /* Front */
  .card-front { background: var(--paper); }
  .card-front .curves { position: absolute; inset: 0; }
  .card-front .brand {
    position: absolute; left: 150px; top: 190px; color: var(--ink);
  }
  .card-front .brand .wordmark { display: flex; align-items: center; gap: 12px; color: var(--maroon); }
  .card-front .tagline {
    margin-top: 14px; font-weight: 700; font-size: 24px; color: var(--ink);
  }
  .person {
    position: absolute; right: 70px; top: 70px; text-align: left;
  }
  .person-name { font-weight: 700; font-size: 30px; color: var(--ink); letter-spacing: 0.5px; }
  .person-title { margin-top: 6px; font-size: 18px; color: var(--ink-soft); }
  .contacts {
    position: absolute; left: 570px; top: 280px; list-style: none;
    color: var(--paper); font-size: 17px;
  }
  .contacts li { display: flex; align-items: center; gap: 12px; margin-bottom: 14px; }
  .contacts svg { width: 16px; height: 16px; flex: none; }
</style>
</head>
<body>
<main class="sheet">

  <section class="card card-back" aria-label="Card back">
    <div class="wordmark">
      <span class="wordmark-square"></span>
      <span class="wordmark-name">BLUE HAVEN</span>
    </div>
    <div class="web-band">
      <svg width="18" height="18" viewBox="0 0 20 20" fill="none" stroke="currentColor" stroke-width="1.6" aria-hidden="true">
        <circle cx="10" cy="10" r="8"/><ellipse cx="10" cy="10" rx="3.5" ry="8"/><line x1="2" y1="10" x2="18" y2="10"/>
      </svg>
      <span class="web-address">www.dravinholdings.example/blue-haven</span>
    </div>
  </section>

  <section class="card card-front" aria-label="Card front">
    <svg class="curves" viewBox="0 0 900 514" preserveAspectRatio="none" aria-hidden="true">
      <path d="M0,170 C60,240 110,380 130,514 L0,514 Z" fill="var(--maroon)"/>
      <path d="M290,514 C370,420 420,260 560,210 C680,168 800,178 900,168 L900,514 Z" fill="var(--maroon)"/>
      <path d="M275,514 C355,410 410,248 555,196 C680,152 800,164 900,154" fill="none" stroke="var(--maroon-line)" stroke-width="3"/>
    </svg>

    <div class="brand">
      <div class="wordmark">
        <span class="wordmark-square"></span>
        <span class="wordmark-name">BLUE HAVEN</span>
      </div>
      <p class="tagline">A Dravin Company</p>
    </div>

    <div class="person">
      <p class="person-name">MARA LENNING</p>
      <p class="person-title">Operation Manager</p>
    </div>

    <ul class="contacts">
      <li>
        <svg viewBox="0 0 16 16" fill="currentColor" aria-hidden="true"><path d="M3 1h3l1.5 4-2 1.2a9 9 0 0 0 4.3 4.3L11 8.5l4 1.5v3a2 2 0 0 1-2 2A12 12 0 0 1 1 3a2 2 0 0 1 2-2z"/></svg>
        <span>+00 555 010 200</span>
      </li>
      <li>
        <svg viewBox="0 0 16 16" fill="none" stroke="currentColor" stroke-width="1.5" aria-hidden="true"><rect x="1.5" y="3.5" width="13" height="9"/><path d="M1.5 3.5 8 9l6.5-5.5"/></svg>
        <span>name@bluehaven.example</span>
      </li>
      <li>
        <svg viewBox="0 0 16 16" fill="currentColor" aria-hidden="true"><path d="M8 1a5 5 0 0 1 5 5c0 4-5 9-5 9S3 10 3 6a5 5 0 0 1 5-5zm0 3a2 2 0 1 0 0 4 2 2 0 0 0 0-4z"/></svg>
        <span>12 Harbour Lane, North District<br>City Name 4021</span>
      </li>
    </ul>
  </section>

</main>
</body>
</html>
```